Healthy living company needs logo / business card

We are looking for a business identity for our company that operates in the Health and Wellness area.
Our audience is those open to hearing about the links between ill health and chemicals in the home as well as how to boost their health naturally through nutrition. We show people how to eliminate those toxins and share the message with others.
We also work with and mentor people who want to build their own business, share the message and create a leveraged income.
Our business name is: Brivora
The tag line we have is: Simple Changes ยท Healthy Living
Output for the project is:
Logo and business card design (2 people on the card).
Our perspective is for a modern, natural, simple, clean design (web 2.0 feel) that will appeal to a broad age range and audience. It should feel professional but not formal. It should not seem medical.
The logo should not be a gradient nor overly complex. Colouring should only be one or two colours at most. They can be bright, we are tending to lean towards green for obvious reasons but open to your thoughts.
Simplicity is the key.
The business card needs to be two sided. We like having the logo and card details on the front and then reversed out on the back with the logo and name in white on the colour block.
Please see the attached card brief document about the card content.

```html
<!DOCTYPE html>
<html lang="en">
<head>
<meta charset="utf-8">
<title>Brivora business card</title>
<link rel="stylesheet" href="https://fonts.googleapis.com/css2?family=Fira+Sans:wght@300;400;500;600&display=swap">
<style>
  :root {
    --leaf-green: #4cb848;
    --paper: #ffffff;
    --card-edge: #d4d4d4;
    --text-font: "Fira Sans", Arial, sans-serif;
  }
  * { margin: 0; padding: 0; box-sizing: border-box; }
  html, body {
    width: 1200px; height: 960px; overflow: hidden;
    background: var(--paper);
    font-family: var(--text-font);
  }
  .sheet { position: relative; width: 1200px; height: 960px; }

  .card {
    position: absolute; left: 286px; width: 756px; height: 434px; overflow: hidden;
  }
  .card--front { top: 16px; background: var(--paper); border: 2px solid var(--card-edge); }
  .card--back  { top: 506px; background: var(--leaf-green); }

  .side-band { position: absolute; bottom: 0; }
  .card--front .side-band { left: 0; top: 72px; width: 38px; background: var(--leaf-green); }
  .card--back .side-band  { left: 714px; top: 74px; width: 24px; background: var(--paper); }

  .wordmark {
    position: absolute; font-weight: 500; line-height: 1; letter-spacing: -1px; white-space: nowrap;
  }
  .tagline {
    position: absolute; font-weight: 300; line-height: 1; white-space: nowrap;
  }
  .tagline .dot { font-weight: 600; }

  .card--front .wordmark { left: 108px; top: 26px; font-size: 134px; color: var(--leaf-green); }
  .card--front .tagline  { left: 110px; top: 166px; font-size: 39px; color: var(--leaf-green); }

  .card--back .wordmark { left: 26px; top: 290px; font-size: 72px; color: var(--paper); }
  .card--back .tagline  { left: 28px; top: 366px; font-size: 21px; color: var(--paper); }

  .person {
    position: absolute; left: 110px; color: var(--leaf-green); font-size: 23px; line-height: 24px;
  }
  .person__name { font-weight: 600; display: block; margin-bottom: 6px; }
  .person__phone { font-weight: 400; display: block; }
  .person--first  { top: 252px; }
  .person--second { top: 334px; }

  .contact {
    position: absolute; left: 426px; top: 246px; list-style: none;
    color: var(--leaf-green); font-weight: 300; font-size: 23px; line-height: 52px;
  }

  .benefits {
    position: absolute; right: 58px; top: 100px; list-style: none; text-align: right;
    color: var(--paper); font-weight: 300; font-size: 21px; line-height: 30px;
  }
</style>
</head>
<body>
<main class="sheet">
  <section class="card card--front" aria-label="Card front">
    <div class="side-band"></div>
    <div class="wordmark">brivora</div>
    <div class="tagline">small shifts <span class="dot">•</span> brighter living</div>

    <div class="person person--first">
      <span class="person__name">Name Name</span>
      <span class="person__phone">555.014.2281</span>
    </div>
    <div class="person person--second">
      <span class="person__name">Name Name</span>
      <span class="person__phone">555.019.6043</span>
    </div>

    <ul class="contact">
      <li>emailaddress@email.com</li>
      <li>555.017.3390</li>
      <li>livebrivora.com</li>
    </ul>
  </section>

  <section class="card card--back" aria-label="Card back">
    <div class="side-band"></div>
    <ul class="benefits">
      <li>multiple streams of income</li>
      <li>financial freedom</li>
      <li>own my own business</li>
      <li>more time</li>
      <li>personal development</li>
      <li>health and vitality</li>
      <li>help others</li>
      <li>meet new people</li>
      <li>retirement plan</li>
      <li>leave a legacy</li>
    </ul>
    <div class="wordmark">brivora</div>
    <div class="tagline">small shifts <span class="dot">•</span> brighter living</div>
  </section>
</main>
</body>
</html>
```